Brisk Ember - Stock Certificate

We need a custom designed stock certificate that represents the look of our company logo but also have a cool look compared to a standard stock certificate. We thinking we want the logo in gold. Our website is https://www.briskemberusa.example.

We are wanting the certificate to look very professional and really cool, we have sales agents that work for the company and we are creating a program by which the sales agents can gain ownership in the company. So the certificates need to have a very cool appeal and that provides a sense of pride in owning "Units" in Brisk Ember.

Reason: Extending so other board members can vote as well, thank you all!

Target Market(s)

Stock/Shareholders

Industry/Entity Type

It Company

Font styles to use
Script

Requirements
Must have
• Must look like a stock certificate, must use our logo which the psd file for it was attached.
Nice to have
• Nice to have the logo in gold

```html
<!DOCTYPE html>
<html lang="en">
<head>
<meta charset="utf-8">
<title>Brisk Ember – Stock Certificate</title>
<link href="https://fonts.googleapis.com/css2?family=Felipa&display=swap" rel="stylesheet">
<style>
  :root {
    --ink: #1f1613;
    --paper-light: #f0c792;
    --paper: #dcaa73;
    --paper-deep: #c99559;
    --border-dark: #2a1f1b;
    --border-gold: #c9955a;
    --band-bronze: #a97b4c;
    --band-dark: #2b2220;
    --seal-text: #e2b36f;
  }
  * { margin: 0; padding: 0; box-sizing: border-box; }
  html, body { width: 1200px; height: 927px; overflow: hidden; background: #ffffff; }
  .certificate {
    position: relative;
    width: 1200px;
    height: 927px;
    font-family: "Felipa", cursive;
    color: var(--ink);
  }
  .certificate__frame {
    position: absolute;
    inset: 0;
    background: linear-gradient(135deg, var(--border-gold), #8a6236 50%, var(--border-gold));
  }
  .certificate__frame::after {
    content: "";
    position: absolute;
    inset: 6px;
    border: 2px solid var(--border-dark);
  }
  .certificate__paper {
    position: absolute;
    left: 37px; top: 37px; right: 37px; bottom: 37px;
    background: linear-gradient(100deg, var(--paper-light) 0%, var(--paper) 45%, var(--paper-deep) 100%);
    border: 2px solid var(--border-dark);
  }
  .band {
    position: absolute;
    top: 37px; bottom: 37px;
    left: 127px; width: 123px;
    background: var(--band-bronze);
  }
  .band__core {
    position: absolute;
    top: 0; bottom: 0;
    left: 17px; width: 89px;
    background: var(--band-dark);
  }
  .seal { position: absolute; left: 60px; top: 72px; width: 250px; height: 250px; }
  .seal__name {
    position: absolute;
    left: 60px; top: 172px; width: 250px;
    text-align: center;
    font-size: 30px;
    color: var(--seal-text);
  }
  .title {
    position: absolute;
    left: 287px; width: 860px; top: 118px;
    text-align: center;
    font-size: 88px;
    line-height: 1;
  }
  .lead {
    position: absolute;
    left: 287px; width: 860px; top: 262px;
    text-align: center;
    font-size: 37px;
  }
  .field-text {
    position: absolute;
    font-size: 34px;
    line-height: 1;
    white-space: nowrap;
  }
  .blank {
    position: absolute;
    height: 0;
    border-top: 2px solid var(--ink);
  }
</style>
</head>
<body>
<main class="certificate">
  <div class="certificate__frame" role="img" aria-label="Dark zigzag pattern border on gold"></div>
  <div class="certificate__paper"></div>

  <div class="band"><div class="band__core"></div></div>

  <svg class="seal" viewBox="0 0 250 250" aria-hidden="true">
    <circle cx="125" cy="125" r="124" fill="#a97b4c"/>
    <circle cx="125" cy="125" r="108" fill="#2b2220"/>
  </svg>
  <div class="seal__name">brisk ember</div>

  <h1 class="title">stock certificate</h1>
  <p class="lead">This is to certify that</p>

  <div class="blank" style="left:287px; width:860px; top:380px;"></div>

  <span class="field-text" style="left:278px; top:436px;">Is the owner of</span>
  <div class="blank" style="left:519px; width:209px; top:472px;"></div>
  <span class="field-text" style="left:732px; top:436px;">shares fo stock of</span>
  <div class="blank" style="left:978px; width:158px; top:472px;"></div>

  <div class="blank" style="left:292px; width:450px; top:563px;"></div>
  <span class="field-text" style="left:744px; top:528px;">on the</span>
  <div class="blank" style="left:832px; width:186px; top:563px;"></div>
  <span class="field-text" style="left:1020px; top:528px;">day of</span>

  <div class="blank" style="left:287px; width:158px; top:654px;"></div>
  <span class="field-text" style="left:451px; top:618px;">In the year</span>
  <div class="blank" style="left:641px; width:128px; top:654px;"></div>
  <span class="field-text" style="left:774px; top:618px;">At</span>
  <div class="blank" style="left:823px; width:315px; top:654px;"></div>
  <span class="field-text" style="left:1142px; top:618px;">.</span>

  <span class="field-text" style="left:677px; top:724px;">Signed,</span>
  <div class="blank" style="left:811px; width:320px; top:760px;"></div>

  <span class="field-text" style="left:681px; top:801px;">Signed,</span>
  <div class="blank" style="left:815px; width:320px; top:837px;"></div>
</main>
</body>
</html>
```